Company brochure for Kestrel & Varden Works, Inc.

We need a company brochure that lets referral sources know who we are, where are locations are and what services we offer. Our website is www.kandvworksinc.com and we are on Facebook and Instagram. We need the brochure to feature both braces and prosthetics.

```html
<!DOCTYPE html>
<html lang="en">
<head>
<meta charset="utf-8">
<title>Kestrel &amp; Varden Works, Inc. — Brochure</title>
<link rel="stylesheet" href="https://fonts.googleapis.com/css2?family=Montserrat:wght@400;500;600;700;800&family=Oswald:wght@500;600&display=swap">
<style>
  :root{
    --navy:#0c3f98;
    --navy-deep:#08317c;
    --orange:#e8561c;
    --sky:#dcebf7;
    --sky-light:#eef5fb;
    --ink:#1f2b3a;
    --ink-soft:#4a5666;
    --white:#ffffff;
    --stage:#e6e8eb;
  }
  *{box-sizing:border-box;margin:0;padding:0}
  html,body{width:1200px;height:900px;overflow:hidden}
  body{background:var(--stage);font-family:"Montserrat",sans-serif;color:var(--ink);position:relative}
  .spread{position:absolute;top:226px;width:580px;height:448px;display:flex;box-shadow:0 4px 14px rgba(0,0,0,.18)}
  .spread--outside{left:13px}
  .spread--inside{left:607px}
  .panel{position:relative;width:193.33px;height:448px;overflow:hidden}
  .panel--light{background:linear-gradient(160deg,var(--sky-light),var(--sky))}
  .panel--navy{background:linear-gradient(180deg,var(--navy),var(--navy-deep));color:var(--white)}
  .pad{padding:14px 13px}
  p,li{font-size:4.6px;line-height:1.45;color:var(--ink-soft)}
  .panel--navy p{color:#dfe8f7}
  .h-display{font-weight:800;color:var(--navy);line-height:1.05}
  .accent{color:var(--orange)}
  .underline{display:block;height:2px;background:var(--orange);border-radius:2px;margin:4px 0 8px}

  /* welcome flap */
  .welcome-title{font-size:17px;color:var(--orange);font-weight:800;margin-top:40px}
  .welcome-sub{font-size:11.5px;font-weight:800;color:var(--navy);line-height:1.15}
  .welcome-flap .underline{width:80px}
  .checklist{list-style:none;margin:5px 0 0 8px}
  .checklist li{position:relative;padding-left:6px;margin-bottom:1.5px}
  .checklist li::before{content:"✓";position:absolute;left:0;color:var(--navy);font-size:4.6px}
  .section-h{font-size:11px;font-weight:500;color:var(--navy);line-height:1.2;margin:26px 0 8px}
  .welcome-flap p+p{margin-top:5px}

  /* contact */
  .contact{text-align:center}
  .map-frame{width:96px;height:96px;border-radius:50%;border:2px solid var(--orange);margin:52px auto 0;padding:3px}
  .map-fill{width:100%;height:100%;border-radius:50%;background:radial-gradient(circle at 40% 45%,#f4f6f8,#d9dee4)}
  .contact-kicker{font-size:6.5px;font-weight:600;color:var(--orange);margin-top:18px}
  .contact-title{font-size:17px;font-weight:800;color:var(--white)}
  .contact .underline{width:22px;margin:4px auto 10px}
  .contact-item{margin-bottom:9px}
  .contact-icon{display:block;width:9px;height:9px;margin:0 auto 4px}
  .contact-text{font-size:5.2px;color:var(--white);letter-spacing:.2px;line-height:1.4}
  .building{width:100px;height:54px;margin:18px auto 0;border:1px solid var(--orange);padding:3px}
  .building-fill{width:100%;height:100%;background:linear-gradient(180deg,#9cc4e6 0,#b9d2e6 40%,#a25a45 41%,#8c4c3a 75%,#6d7378 76%)}

  /* cover */
  .cover-art{position:absolute;inset:0}
  .cover-body{position:absolute;left:12px;right:10px;top:245px}
  .brand-mark{display:flex;align-items:center;gap:5px;margin-left:10px}
  .brand-dot{width:22px;height:22px;border-radius:50%;background:var(--navy)}
  .brand-name{font-family:"Montserrat",sans-serif;font-weight:600;font-size:6.4px;color:var(--navy);line-height:1.2}
  .cover-welcome{font-family:"Oswald",sans-serif;font-weight:600;font-size:17px;color:var(--orange);line-height:1.1;margin-top:18px}
  .cover-name{font-family:"Oswald",sans-serif;font-weight:500;font-size:12.5px;color:var(--navy);line-height:1.15}
  .cover-tag{font-size:7px;color:var(--ink);line-height:1.3;margin-top:4px}
  .cover-rule{width:60px;height:2px;background:var(--navy);margin:7px 0 8px}
  .web{font-size:7px;font-weight:500;color:var(--ink)}
  .web .accent{color:var(--orange)}

  /* info panel */
  .info-title{font-size:15px;font-weight:700;color:var(--white);line-height:1.12;margin-top:22px}
  .info .underline{width:78px;margin-bottom:10px}
  .info-h{font-size:9.5px;font-weight:500;color:var(--white);line-height:1.2;margin:12px 0 5px}
  .info p strong{color:var(--white);font-weight:600}
  .info p+p{margin-top:5px}

  /* about */
  .about-h{font-size:9.5px;font-weight:800;color:var(--navy);margin:12px 0 3px}
  .about-h:first-child{margin-top:4px}
  .about p+p{margin-top:5px}
  .about-photos{position:absolute;left:0;bottom:0;width:193.33px;height:175px}

  /* services */
  .services-title{font-size:15px;margin-top:14px}
  .services .underline{width:72px;margin-bottom:12px}
  .service{display:flex;justify-content:space-between;align-items:center;margin-bottom:17px}
  .service-copy{width:112px}
  .service-h{font-size:7.4px;font-weight:700;color:var(--ink);margin-bottom:3px}
  .service-icon{width:30px;height:26px;border-radius:5px;background:linear-gradient(135deg,#f08a4a,#c9d9ee)}
  .service-icon--clock{background:linear-gradient(135deg,#7aa6dd,#cfe0f3)}
  .service-icon--product{background:linear-gradient(135deg,#3b4e6e,#d9a06a)}
  .move-h{font-size:12.5px;font-weight:700;color:var(--navy);line-height:1.05;margin-top:18px}
  .move-h .accent{display:block}
  .services p{margin-top:4px}
  .services .brand-mark{justify-content:center;margin:14px 0 8px}
  .services .web{text-align:center;font-size:8px}
</style>
</head>
<body>

<!-- OUTSIDE SPREAD -->
<section class="spread spread--outside" aria-label="Brochure outside spread">

  <article class="panel panel--light welcome-flap">
    <div class="pad">
      <h2 class="welcome-title">Welcome to</h2>
      <p class="welcome-sub">Kestrel &amp; Varden<br>Works, Inc.</p>
      <span class="underline"></span>
      <p>Thank you for choosing K&amp;V Works, Inc. for your orthotic and prosthetic needs. We pride ourselves on providing each and every one of our patients with high quality care and service under the direction of your physician. Our qualified and friendly staff is ready to aid you with all your questions.</p>
      <p>To help you prepare for your first visit we have created a Patient Information page to explain the process and prepare you for your first visit.</p>
      <ul class="checklist">
        <li>Patient Information Form</li>
        <li>Assignment of Benefits</li>
        <li>PCP-Patient Contact Preference/Medicare History</li>
        <li>Medicare Supplier Standards</li>
        <li>Medical Release</li>
        <li>Summary of Notice of Privacy Practices</li>
      </ul>
      <h3 class="section-h">What to expect at your<br>first appointment.</h3>
      <p>When you call one of our 7 convenient offices our friendly OA's will ask you about your specific situation so that we can assess how much time will be needed for your appointment to schedule you. The OA will ask for your insurance information, what your diagnosis is, referring physician's name and what item your physician is prescribing and whether or not you have a written prescription advising what needs to be provided. We will then schedule an appointment time at a location that is convenient for you.</p>
      <p>Plan on arriving 10-15 minutes early to fill out any forms that are needed.</p>
    </div>
  </article>

  <article class="panel panel--navy contact">
    <div class="map-frame"><div class="map-fill" role="img" aria-label="Street map showing the office location"></div></div>
    <p class="contact-kicker">Get in touch</p>
    <h2 class="contact-title">Contact</h2>
    <span class="underline"></span>
    <div class="contact-item">
      <svg class="contact-icon" viewBox="0 0 10 10" aria-hidden="true"><circle cx="5" cy="5" r="5" fill="#e8561c"/><circle cx="5" cy="5" r="2.6" fill="none" stroke="#fff" stroke-width=".7"/><path d="M2.4 5h5.2M5 2.4c-1.2 1.4-1.2 3.8 0 5.2M5 2.4c1.2 1.4 1.2 3.8 0 5.2" fill="none" stroke="#fff" stroke-width=".5"/></svg>
      <p class="contact-text">WWW.KANDVWORKSINC.COM</p>
    </div>
    <div class="contact-item">
      <svg class="contact-icon" viewBox="0 0 10 10" aria-hidden="true"><circle cx="5" cy="5" r="5" fill="#e8561c"/><path d="M3.3 2.8c.3-.3.7-.3.9 0l.5.7c.2.3.1.6-.1.8l-.3.3c.3.7.8 1.2 1.4 1.5l.3-.3c.2-.2.5-.3.8-.1l.7.5c.3.2.3.6 0 .9l-.4.4c-1.7.4-4.2-2.1-3.8-3.8z" fill="#fff"/></svg>
      <p class="contact-text">(555) 014-2290</p>
    </div>
    <div class="contact-item">
      <svg class="contact-icon" viewBox="0 0 10 10" aria-hidden="true"><circle cx="5" cy="5" r="5" fill="#e8561c"/><path d="M5 2.2a2 2 0 0 1 2 2c0 1.5-2 3.6-2 3.6S3 5.7 3 4.2a2 2 0 0 1 2-2z" fill="#fff"/><circle cx="5" cy="4.2" r=".7" fill="#e8561c"/></svg>
      <p class="contact-text">120 ALDER ROW,<br>BROOKFIELD, MO 63000-0142</p>
    </div>
    <div class="building"><div class="building-fill" role="img" aria-label="Photo of the office building and parking lot"></div></div>
  </article>

  <article class="panel panel--light cover">
    <svg class="cover-art" viewBox="0 0 193.33 448" preserveAspectRatio="none">
      <defs>
        <linearGradient id="coverPhoto" x1="0" y1="0" x2="0" y2="1">
          <stop offset="0" stop-color="#e9eef3"/>
          <stop offset=".55" stop-color="#c8d3de"/>
          <stop offset="1" stop-color="#8fa5bd"/>
        </linearGradient>
      </defs>
      <path d="M0 0H193.33V268C160 250 130 215 90 190C60 172 25 160 0 150Z" fill="url(#coverPhoto)" role="img" aria-label="Photo of the clinical team and patients standing together"/>
      <path d="M0 148C28 156 62 168 92 188C132 214 162 248 193.33 266V276C160 262 128 228 88 202C58 182 26 170 0 162Z" fill="#0c3f98"/>
    </svg>
    <div class="cover-body">
      <div class="brand-mark"><span class="brand-dot"></span><span class="brand-name">Kestrel &amp; Varden<br>Works, Inc.</span></div>
      <h1 class="cover-welcome">Welcome to</h1>
      <p class="cover-name">Kestrel &amp; Varden Works</p>
      <p class="cover-tag">Where we create custom made<br>solutions that work for you!</p>
      <div class="cover-rule"></div>
      <p class="web">www.<span class="accent">kandvworksinc</span>.com</p>
    </div>
  </article>
</section>

<!-- INSIDE SPREAD -->
<section class="spread spread--inside" aria-label="Brochure inside spread">

  <article class="panel panel--navy info">
    <div class="pad">
      <h2 class="info-title">What information<br>should you bring?</h2>
      <span class="underline"></span>
      <p>You should bring the forms that you filled out from this website along with your insurance card, the prescription that your physician provided you, X-rays (if asked to bring them when making the appointment). If you already have an orthotic or prosthetic device previously worn make sure to bring that with you even if worn out, broken or outgrown. If your device goes in a shoe, bring the shoes you plan to wear most often with the device. You can have a family member or friend accompany you if you would like. They will help you with instructions and questions you may not think to ask.</p>
      <h3 class="info-h">What to expect during your appointment.</h3>
      <p>After filling out the proper paperwork one of our OA's will weigh you and take your height (this is needed to show growth, weight gain/loss for insurance coverage). You will then be shown to an exam room and one of our practitioners will do a complete evaluation. They will discuss your options based on your needs and your insurance coverage. You will be measured or cast depending on your needs.</p>
      <h3 class="info-h">Insurance Benefits</h3>
      <p>Our charges are not subject to an office visit co-pay, we bill under your insurance policy's DME or Orthotic benefits. The OA at the front desk will verify your insurance benefits and will explain the quote to you, including any estimated co-insurance based on your carriers quote. Most insurance policies require the insured to be responsible for a percentage of the total amount charged after their contracted discount along with an annual deductible. <strong>You will be responsible to pay half down on your co-insurance to start the work on your device and the balance will be due when you are fit with the device. If you are fit the same day then you will be asked to pay the co-insurance at that time.</strong></p>
      <p><strong>"We urge you to be proactive and contact your insurance carrier prior to your appointment to verify your benefits/coverage for orthotic and/or prosthetics along with any deductible that may apply. This will make you better informed. If you need help with codes or procedures our OA's will be happy to assist you.</strong></p>
    </div>
  </article>

  <article class="panel panel--light about">
    <div class="pad">
      <h2 class="about-h">About <span class="accent">Us</span></h2>
      <p>Kestrel &amp; Varden Works has been providing quality, compassionate care to residents of St. Louis and Southern Illinois since 1983. A recognized leader in the field, our experts work as a team to create the most functional solution to your orthotic, prosthetic and pedorthic needs using the latest technology available. Our patient-centered, team approach means we work closely with your doctor, nurse, therapist and family to create custom made solutions that work for you.</p>
      <p>Our practitioners make up the largest and most experienced K &amp; V practice in the area. We have both adult and pediatric specialists. Our board-certified practitioners regularly attend and conduct continuing education programs and clinics allowing us to bring our patients the very latest in technology and developments in the field. Our central fabrication facility allows us to fabricate your device with speed, quality, and convenience.</p>
      <h2 class="about-h">Our <span class="accent">Mission</span></h2>
      <p>We are people committed to using every scientific and technical development available to restore the physical capabilities of the disabled. By combining intellectual know-how and modern technology we seek to help the "disabled" become "enabled".</p>
      <p>Our pledge is to use all of our orthotic and prosthetic resources to empower individuals with physical challenges to participate in all facets of life.</p>
    </div>
    <svg class="about-photos" viewBox="0 0 193.33 175" preserveAspectRatio="none">
      <defs>
        <linearGradient id="walkPhoto" x1="0" y1="0" x2="0" y2="1"><stop offset="0" stop-color="#8f8c6e"/><stop offset="1" stop-color="#5a4a3c"/></linearGradient>
        <linearGradient id="babyPhoto" x1="0" y1="0" x2="1" y2="1"><stop offset="0" stop-color="#f1dccb"/><stop offset="1" stop-color="#c9a88f"/></linearGradient>
        <linearGradient id="fitPhoto" x1="0" y1="0" x2="1" y2="1"><stop offset="0" stop-color="#e58a3c"/><stop offset="1" stop-color="#8c4a2a"/></linearGradient>
      </defs>
      <path d="M0 0C40 10 70 30 100 60C130 92 160 120 193.33 130V175H0Z" fill="url(#walkPhoto)" role="img" aria-label="Photo of a person walking outdoors with a prosthetic leg"/>
      <path d="M0 0C40 10 70 30 100 60C130 92 160 120 193.33 130" fill="none" stroke="#0c3f98" stroke-width="4"/>
      <circle cx="70" cy="40" r="33" fill="url(#babyPhoto)" stroke="#0c3f98" stroke-width="3" role="img" aria-label="Photo of an infant wearing a cranial helmet"/>
      <circle cx="150" cy="95" r="28" fill="url(#fitPhoto)" stroke="#0c3f98" stroke-width="3" role="img" aria-label="Photo of a child being fitted for leg braces"/>
    </svg>
  </article>

  <article class="panel panel--light services">
    <div class="pad">
      <h2 class="h-display services-title">Services <span class="accent">Us</span></h2>
      <span class="underline"></span>
      <div class="service">
        <div class="service-copy">
          <h3 class="service-h">Insurance Contracts</h3>
          <p>We are contracted with almost all local insurance plans and offer comprehensive insurance billing for the convenience of our patients.</p>
        </div>
        <div class="service-icon" role="img" aria-label="Illustration of a medical folder"></div>
      </div>
      <div class="service">
        <div class="service-copy">
          <h3 class="service-h">Locations &amp; Hours</h3>
          <p>With 7 offices in the Metropolitan area we have a location near you.</p>
        </div>
        <div class="service-icon service-icon--clock" role="img" aria-label="Illustration of a clock and magnifier"></div>
      </div>
      <div class="service">
        <div class="service-copy">
          <h3 class="service-h">Our Products</h3>
          <p>We offer the very best in Orthotic, Prosthetic and Pedorthic devices.</p>
        </div>
        <div class="service-icon service-icon--product" role="img" aria-label="Illustration of braces and a prosthetic foot"></div>
      </div>
      <h2 class="move-h">MOVE NATURALLY <span class="accent">SAFETY</span></h2>
      <p>With powered toe lift and stumble recovery to help reduce the risk of trips and falls.</p>
      <p>After 32 years of trips and falls as an amputee, Dale Morrow learned to avoid certain terrain - like ramps, grass and mulch - whenever possible. But things changed the day Dale switched to STRIDELINE LEG. Now, he says, "I don't really think about the terrain I'm walking on. It's not an issue. I feel so safe walking on STRIDELINE LEG that I am more active than I have been in decades."</p>
      <div class="brand-mark"><span class="brand-dot"></span><span class="brand-name">Kestrel &amp; Varden<br>Works, Inc.</span></div>
      <p class="web">www.<span class="accent">kandvworksinc</span>.com</p>
    </div>
  </article>
</section>

</body>
</html>
```